Postcard Design for BQAV-

We need a postcard designed that is similar to our current example with information but has a few changes for the season. It needs to be an oversized postcard that meets KRTL BQAV requirements.

In the section that says complete car care, I'd like to add a blurb that Summer is here! Make sure your Car is ready and your:
AC is cold
Cooling system is functioning properly
Tires and Alighment are vacation ready

Elsewhere on the card, we need to add that we offer a 3 year/36,000 warranty on parts and labor

We also need to add that we have a 5.0 Zorvia Review Score and a 4.9 Pavo Nimbal score

Colors can change as can font as long as it is easy to read

```html
<!DOCTYPE html>
<html lang="en">
<head>
<meta charset="utf-8">
<title>Tandem Gear Auto Repair – BQAV Postcard</title>
<link rel="stylesheet" href="https://fonts.googleapis.com/css2?family=Unbounded:wght@800;900&family=Poppins:ital,wght@0,400;0,500;0,600;0,700;1,700&family=Great+Vibes&display=swap">
<style>
:root{
  --green:#7ab648;
  --green-dark:#5f9a33;
  --sky:#5ec4ef;
  --ink:#1d1d1b;
  --text:#333;
  --paper:#fff;
  --stage:#6e6e6e;
  --steel-a:#e9ecef;
  --steel-b:#9aa1a8;
  --warranty-red:#c8202f;
  --star:#f5a623;
}
*{margin:0;padding:0;box-sizing:border-box}
html,body{width:1200px;height:749px;overflow:hidden;background:var(--stage)}
body{position:relative;font-family:"Poppins",sans-serif;color:var(--ink)}
.card{position:absolute;top:184px;width:570px;height:380px;background:var(--paper);overflow:hidden;box-shadow:0 6px 14px rgba(0,0,0,.35)}
.card--front{left:20px}
.card--back{left:610px}
.abs{position:absolute}

/* shared decor */
.wrench{position:absolute;height:10px;border-radius:5px;background:linear-gradient(180deg,var(--steel-a),var(--steel-b));transform-origin:left center;box-shadow:1px 2px 3px rgba(0,0,0,.25)}

/* FRONT */
.brand{left:26px;top:30px;display:flex;align-items:center;gap:7px}
.brand__dot{width:16px;height:16px;border-radius:50%;background:var(--ink)}
.brand__name{font-weight:700;font-size:15px;line-height:1.05;color:var(--ink);letter-spacing:.3px}
.brand__phone{left:49px;top:69px;font-size:10px;font-weight:600;color:var(--ink)}
.perk-banner{left:350px;top:23px;width:230px;height:50px;background:var(--green);clip-path:polygon(6% 0,100% 0,100% 100%,0 100%);color:var(--ink);font-size:15.5px;line-height:1.15;padding:7px 0 0 38px}
.kicker{left:142px;top:104px;font-size:19px;color:var(--green)}
.headline{font-family:"Unbounded",sans-serif;font-weight:900;line-height:1;letter-spacing:-1px}
.headline--auto{left:24px;top:132px;font-size:54px;color:var(--ink)}
.headline--repair{left:24px;top:186px;font-size:54px;color:var(--green)}
.amp{left:40px;top:222px;font-size:36px;color:var(--green);font-weight:400}
.subhead{left:91px;top:237px;font-size:20px;font-weight:500;line-height:1.05;letter-spacing:.6px;color:var(--ink)}
.photo{left:400px;top:150px;width:170px;height:230px;background:linear-gradient(160deg,#c9ccd0 0%,#8a939c 40%,#3f4a57 70%,#6d2a2a 100%);clip-path:polygon(40% 0,100% 0,100% 100%,0 100%,0 78%)}
.warranty{left:385px;top:100px;width:114px;height:114px;border-radius:50%;background:var(--paper);border:2px solid var(--sky);box-shadow:0 0 0 3px var(--paper),0 0 0 4px var(--sky);text-align:center;padding-top:22px}
.warranty__lead{font-size:11.5px;line-height:1.1}
.warranty__term{font-size:12px;font-weight:600;color:var(--green-dark)}
.warranty__word{font-family:"Great Vibes",cursive;font-size:22px;line-height:.9;color:var(--warranty-red)}
.warranty__tag{display:inline-block;margin-top:2px;background:var(--green);color:#fff;font-size:8px;padding:1px 6px;border-radius:7px}
.info-band{left:0;top:306px;width:340px;height:46px;background:var(--sky);padding:7px 0 0 24px;font-size:11px;line-height:1.55;letter-spacing:.3px;color:var(--ink)}
.info-band div{display:flex;align-items:center;gap:8px;white-space:nowrap}
.info-band svg{width:9px;height:9px;flex:none}
.call-box{left:302px;top:293px;width:182px;height:72px;background:var(--green);border-radius:10px;transform:skewX(-12deg);box-shadow:0 0 0 3px var(--paper)}
.call-text{left:310px;top:300px;width:170px;text-align:center;font-weight:700;color:var(--ink);line-height:1.1}
.call-text__label{font-size:17px}
.call-text__number{font-size:18.5px;color:#fff;margin-top:3px;letter-spacing:.3px}

/* BACK */
.season-banner{left:0;top:23px;width:225px;height:52px;background:var(--green);clip-path:polygon(0 0,92% 0,100% 100%,0 100%);padding:5px 0 0 24px;box-shadow:0 0 0 2px #e5e5e5}
.season-banner__title{font-size:15px;font-weight:700;font-style:italic;color:#fff;line-height:1.05}
.season-banner__body{font-size:11px;line-height:1.05;color:var(--ink);font-weight:500}
.checklist{left:22px;top:80px;list-style:none;font-size:12px;line-height:15px;letter-spacing:.3px;color:var(--ink)}
.checklist li{display:flex;align-items:center;gap:9px;white-space:nowrap}
.checklist svg{width:10px;height:10px;flex:none}
.script{font-family:"Great Vibes",cursive}
.complete{left:28px;top:127px;font-size:26px;line-height:1.1;color:var(--green)}
.headline--car{left:24px;top:158px;font-size:44px;color:var(--ink)}
.headline--care{left:24px;top:202px;font-size:50px;color:var(--green)}
.inspect-band{left:0;top:258px;width:330px;height:26px;background:var(--sky);box-shadow:0 0 0 2px #e5e5e5;padding:4px 0 0 24px;font-size:12px;font-weight:700;letter-spacing:.6px;color:var(--ink);white-space:nowrap}
.blurb{left:24px;top:291px;width:318px;font-size:9px;line-height:1.4;color:var(--text)}
.perk{top:334px;font-size:8.8px;line-height:1.25;color:var(--text);display:flex;gap:5px}
.perk svg{width:8px;height:8px;margin-top:2px;flex:none}
.perk--one{left:24px}
.perk--two{left:175px}
.return-addr{left:369px;top:24px;font-size:7px;line-height:1.55;color:var(--ink)}
.divider{left:470px;top:24px;width:1px;height:40px;background:var(--ink)}
.indicia{left:482px;top:24px;font-size:7px;line-height:1.55;color:var(--ink)}
.postal-band{left:339px;top:74px;width:231px;height:32px;background:var(--sky);padding:5px 0 0 30px;font-size:7px;line-height:1.6;color:var(--ink);box-shadow:0 0 0 2px #e5e5e5}
.reviews{left:349px;top:110px;width:221px;text-align:center}
.reviews__name{font-size:19px;font-weight:500;color:#5b7fd6;line-height:1.2}
.reviews__stars{color:var(--star);font-size:10px;letter-spacing:2px;line-height:1}
.reviews__text{font-size:8.4px;line-height:1.4;color:#777;margin-top:3px}
.map{left:349px;top:180px;width:221px;height:148px;background:linear-gradient(135deg,#dbeedd,#c9d6e0)}
.footer-band{left:352px;top:331px;width:218px;height:28px;background:var(--green);box-shadow:0 0 0 3px var(--paper);font-size:9.2px;line-height:28px;color:var(--ink);padding:0 0 0 12px;white-space:nowrap;letter-spacing:.1px}
</style>
</head>
<body>

<section class="card card--front" aria-label="Postcard front">
  <div class="abs photo" role="img" aria-label="Photo of a mechanic working under the hood of a white car in a repair shop"></div>
  <div class="wrench" role="img" aria-label="Chrome wrench" style="left:315px;top:122px;width:130px;transform:rotate(-40deg)"></div>
  <div class="wrench" role="img" aria-label="Chrome wrench" style="left:322px;top:183px;width:130px;transform:rotate(40deg)"></div>

  <div class="abs brand"><span class="brand__dot"></span><span class="brand__name">TANDEM GEAR<br>AUTO REPAIR</span></div>
  <div class="abs brand__phone">555.014.2287</div>

  <div class="abs perk-banner">Free Vehicle Pick Up,<br>Drop Off &amp; Loaners</div>

  <div class="abs kicker">High-Quality</div>
  <div class="abs headline headline--auto">AUTO</div>
  <div class="abs headline headline--repair">REPAIR</div>
  <div class="abs amp">&amp;</div>
  <div class="abs subhead">Preventative<br>Maintenance!</div>

  <div class="abs warranty">
    <div class="warranty__lead">We offer a</div>
    <div class="warranty__term">3 year / 36,000</div>
    <div class="warranty__word">Warranty</div>
    <div class="warranty__tag">On Parts &amp; Labor</div>
  </div>

  <div class="abs info-band">
    <div><svg viewBox="0 0 10 10"><path d="M5 0a3.5 3.5 0 0 0-3.5 3.5C1.5 6 5 10 5 10s3.5-4 3.5-6.5A3.5 3.5 0 0 0 5 0zm0 5a1.5 1.5 0 1 1 0-3 1.5 1.5 0 0 1 0 3z" fill="#1d1d1b"/></svg>418 Fallow Creek Road, Unit D, Marlow Glen</div>
    <div><svg viewBox="0 0 10 10"><circle cx="5" cy="5" r="4.2" fill="none" stroke="#1d1d1b" stroke-width="1"/><path d="M.8 5h8.4M5 .8c-2 2.5-2 5.9 0 8.4M5 .8c2 2.5 2 5.9 0 8.4" fill="none" stroke="#1d1d1b" stroke-width=".8"/></svg>www.TandemGearRepair.com</div>
  </div>

  <div class="abs call-box"></div>
  <div class="abs call-text">
    <div class="call-text__label">CALL US</div>
    <div class="call-text__number">555-014-2287</div>
  </div>
</section>

<section class="card card--back" aria-label="Postcard back">
  <div class="wrench" role="img" aria-label="Chrome wrench" style="left:262px;top:30px;width:135px;transform:rotate(45deg)"></div>

  <div class="abs season-banner">
    <div class="season-banner__title">Summer is here!</div>
    <div class="season-banner__body">Make sure your Car is<br>ready and your:</div>
  </div>

  <ul class="abs checklist">
    <li><svg viewBox="0 0 10 10"><circle cx="5" cy="5" r="5" fill="#7ab648"/><path d="M2.6 5.1l1.7 1.7 3.2-3.4" fill="none" stroke="#fff" stroke-width="1.3"/></svg>AC is cold</li>
    <li><svg viewBox="0 0 10 10"><circle cx="5" cy="5" r="5" fill="#7ab648"/><path d="M2.6 5.1l1.7 1.7 3.2-3.4" fill="none" stroke="#fff" stroke-width="1.3"/></svg>Cooling system is functioning properly</li>
    <li><svg viewBox="0 0 10 10"><circle cx="5" cy="5" r="5" fill="#7ab648"/><path d="M2.6 5.1l1.7 1.7 3.2-3.4" fill="none" stroke="#fff" stroke-width="1.3"/></svg>Tires and Alighment are vacation ready</li>
  </ul>

  <div class="abs script complete">Complete</div>
  <div class="abs headline headline--car">CAR</div>
  <div class="abs headline headline--care">CARE</div>

  <div class="abs inspect-band">INCLUDING INSPECTIONS AND EMISSIONS</div>
  <p class="abs blurb">Don't trust your car to just any automotive repair shop. We have the reliable, expeirnced technicians to quickly diagnose what's wrong and fix it right the first time - saving you time, headaches and money.</p>
  <div class="abs perk perk--one"><svg viewBox="0 0 10 10"><rect x="1" y="1" width="8" height="8" fill="#7ab648"/></svg><span>Trust in a timely, full-service<br>repair facility.</span></div>
  <div class="abs perk perk--two"><svg viewBox="0 0 10 10"><path d="M1 4h2v5H1zM3.5 4L5.5 .8c.9 0 1.2.8 1 1.6L6 4h2.7c.7 0 1 .6.9 1.1L8.8 8.4c-.1.4-.5.6-.9.6H3.5z" fill="#7ab648"/></svg><span>Enjoy unpairalleled<br>customer service.</span></div>

  <div class="abs return-addr">Tandem Gear Repair 418<br>Fallow Creek Road, Unit D<br>Marlow Glen, PA 17990</div>
  <div class="abs divider"></div>
  <div class="abs indicia">PRSRT STD<br>ECRWSS<br>KRTL POSTAGE<br>PAID BQAV RETAIL</div>

  <div class="abs postal-band">******************ECRWSS****BQAV<br>Local Postal Customer.</div>

  <div class="abs reviews">
    <div class="reviews__name">Zorvia</div>
    <div class="reviews__stars">★★★★★</div>
    <div class="reviews__text">We have a 5.0 Zorvia Review Score<br>&amp; 4.9 Pavo Nimbal Score</div>
  </div>

  <div class="abs map" role="img" aria-label="Street map showing the shop location on Fallow Creek Road"></div>
  <div class="abs footer-band">555-014-2287 &nbsp;|&nbsp; TandemGearRepair.com</div>
</section>

</body>
</html>
```